Need Help having my business card stand out

I am the owner of Brisa Canine Coaching and would like for my business cards to stand out. I have been trying to keep designing them myself but I can't get what I have in my head on the card. I will try my best to post templates that I like for inspirations. I want something unique but elegant. I don't want in to look cartoony or cheesy. It needs to pop in a pet shop but also in a coffee shop or gym.

Target Market(s)

Dog owners, Married ,No young kids Jr High school kids and up (maybe kids on the way) Executives, Stay at home moms/wives, Small business owners

Industry/Entity Type

Dog Training

Contact Information for Business Card

Lorna Whitfield, 555-304-7719, info@brisacanine.example, www.brisacanine.example

Colors

Designer to choose colors to be used in the design.

Requirements
Must have
• my logo
Should not have
• Cursive lettering

```html
<!DOCTYPE html>
<html lang="en">
<head>
<meta charset="utf-8">
<title>Brisa Canine Coaching — Business Card</title>
<link rel="stylesheet" href="https://fonts.googleapis.com/css2?family=Open+Sans:wght@400;700;800&display=swap">
<style>
  :root {
    --backdrop: #e9e7e4;
    --card-white: #f7f7f6;
    --ink: #161616;
    --ink-soft: #2a2a2a;
    --panel-black: #050505;
    --mark-white: #ffffff;
    --photo-grass: #5f7a3a;
    --photo-trees: #a9ab86;
    --photo-shade: #3e4a2c;
  }
  * { margin: 0; padding: 0; box-sizing: border-box; }
  html, body {
    width: 1200px;
    height: 844px;
    overflow: hidden;
    background: var(--backdrop);
    font-family: "Open Sans", Arial, sans-serif;
    color: var(--ink);
  }
  .canvas {
    position: relative;
    width: 1200px;
    height: 844px;
    display: flex;
    align-items: center;
    justify-content: center;
    gap: 60px;
  }
  .card {
    position: relative;
    width: 520px;
    height: 298px;
    overflow: hidden;
    box-shadow: 0 10px 28px rgba(0,0,0,0.18);
  }

  /* Front */
  .card-front { background: var(--card-white); }
  .brand-mark {
    position: absolute;
    top: 52px;
    right: 44px;
    display: flex;
    align-items: center;
    gap: 10px;
  }
  .brand-square {
    width: 18px;
    height: 18px;
    background: var(--ink);
  }
  .brand-name {
    font-weight: 800;
    font-size: 21px;
    line-height: 1.05;
    letter-spacing: 0.01em;
    color: var(--ink);
    width: 150px;
  }
  .holder {
    position: absolute;
    left: 40px;
    bottom: 40px;
  }
  .holder-name {
    font-weight: 700;
    font-size: 18px;
    letter-spacing: 0.02em;
    text-transform: uppercase;
    margin-bottom: 28px;
  }
  .contact-list { list-style: none; }
  .contact-item {
    display: flex;
    align-items: center;
    gap: 8px;
    font-size: 14px;
    line-height: 20px;
    color: var(--ink-soft);
  }
  .contact-icon { width: 12px; height: 12px; flex: none; }

  /* Back */
  .card-back { display: flex; background: var(--panel-black); }
  .photo-area {
    width: 48%;
    height: 100%;
    background: linear-gradient(180deg, var(--photo-trees) 0%, var(--photo-grass) 48%, var(--photo-shade) 100%);
  }
  .back-panel {
    flex: 1;
    display: flex;
    align-items: center;
    justify-content: center;
    gap: 10px;
  }
  .back-panel .brand-square { background: var(--mark-white); }
  .back-panel .brand-name { color: var(--mark-white); }
</style>
</head>
<body>
  <main class="canvas">
    <section class="card card-front" aria-label="Business card front">
      <div class="brand-mark">
        <span class="brand-square"></span>
        <span class="brand-name">Brisa Canine Coaching</span>
      </div>
      <div class="holder">
        <h1 class="holder-name">Lorna Whitfield</h1>
        <ul class="contact-list">
          <li class="contact-item">
            <svg class="contact-icon" viewBox="0 0 24 24" aria-hidden="true"><path fill="currentColor" d="M6.6 10.8a15.1 15.1 0 0 0 6.6 6.6l2.2-2.2a1 1 0 0 1 1-.25 11.4 11.4 0 0 0 3.6.57 1 1 0 0 1 1 1V20a1 1 0 0 1-1 1A17 17 0 0 1 3 4a1 1 0 0 1 1-1h3.5a1 1 0 0 1 1 1c0 1.25.2 2.45.57 3.57a1 1 0 0 1-.25 1z"/></svg>
            <span>555-304-7719</span>
          </li>
          <li class="contact-item">
            <svg class="contact-icon" viewBox="0 0 24 24" aria-hidden="true"><path fill="currentColor" d="M2 5h20v14H2z"/><path fill="none" stroke="#f7f7f6" stroke-width="2" d="M3 6l9 7 9-7"/></svg>
            <span>info@brisacanine.example</span>
          </li>
          <li class="contact-item">
            <svg class="contact-icon" viewBox="0 0 24 24" aria-hidden="true"><circle cx="12" cy="12" r="10" fill="currentColor"/><path fill="none" stroke="#f7f7f6" stroke-width="1.6" d="M2 12h20M12 2c3 3 3 17 0 20M12 2c-3 3-3 17 0 20"/></svg>
            <span>www.brisacanine.example</span>
          </li>
        </ul>
      </div>
    </section>

    <section class="card card-back" aria-label="Business card back">
      <div class="photo-area" role="img" aria-label="Photo of a trainer standing in a sunny park with three dogs sitting attentively"></div>
      <div class="back-panel">
        <span class="brand-square"></span>
        <span class="brand-name">Brisa Canine Coaching</span>
      </div>
    </section>
  </main>
</body>
</html>
```